Business card

I want a business card the looks like a credit card, must eye-catching !!! I attached some things that I did obviously I want it to LOOK WAY more professional than what I can do....Just some ideas.... that I was thinking

Contact Information for Business Card

Must look like a credit card, I attached some things that I did obviously I want it to LOOK WAY more professional than what I can do....Just some ideas.... that I was thinking

Requirements
Must have
• Must look like a credit card, I attached some things that I did obviously I want it to LOOK WAY more professional than what I can do....Just some ideas.... that I was thinking
Nice to have
Should not have

```html
<!DOCTYPE html>
<html lang="en">
<head>
<meta charset="utf-8">
<title>Relay Business Partners – Card-Style Business Card</title>
<link href="https://fonts.googleapis.com/css2?family=Exo+2:ital,wght@0,400;0,500;0,600;0,800;1,800&family=Share+Tech+Mono&display=swap" rel="stylesheet">
<style>
  :root {
    --navy-deep: #0b2547;
    --navy: #123a66;
    --navy-light: #1b4f80;
    --ink: #1f3f6e;
    --gold: #f7c512;
    --chip-light: #f0dc86;
    --chip-dark: #b48f2d;
    --white: #ffffff;
    --strip: #e3e6ea;
    --dot-one: #1d4d7c;
    --dot-two: #8db4e0;
    --dot-three: #1a8fd0;
  }
  * { box-sizing: border-box; margin: 0; padding: 0; }
  html, body { width: 1200px; height: 950px; overflow: hidden; background: var(--white); }
  body { position: relative; font-family: "Exo 2", sans-serif; color: var(--white); }

  .card {
    position: absolute;
    top: 335px;
    width: 488px;
    height: 278px;
    border-radius: 30px;
    overflow: hidden;
    background: linear-gradient(135deg, var(--navy-light) 0%, var(--navy) 45%, var(--navy-deep) 100%);
    box-shadow: 8px 14px 22px rgba(0,0,0,0.35);
  }
  .card--front { left: 79px; }
  .card--back { left: 630px; background: linear-gradient(135deg, var(--navy-deep) 0%, var(--navy) 55%, var(--navy-light) 100%); }

  .map-area {
    position: absolute; inset: 10px 20px 10px 10px;
    background: radial-gradient(ellipse at 50% 45%, rgba(120,160,210,0.12), rgba(120,160,210,0) 70%);
  }

  .chip { position: absolute; left: 27px; top: 61px; width: 56px; height: 49px; }

  .brand { position: absolute; color: var(--gold); font-weight: 800; }
  .brand__tag { position: absolute; font-size: 7px; font-weight: 800; color: var(--white); letter-spacing: 0.1px; white-space: nowrap; }
  .brand__name { position: absolute; display: flex; align-items: center; gap: 8px; white-space: nowrap; line-height: 1; }
  .brand__dot { border-radius: 50%; background: var(--gold); flex: none; }

  .front-brand { left: 178px; top: 24px; width: 290px; height: 90px; }
  .front-brand .brand__name { left: 0; top: 12px; font-size: 36px; }
  .front-brand .brand__dot { width: 26px; height: 26px; }
  .front-brand .brand__sub { position: absolute; left: 78px; top: 52px; font-size: 17px; font-weight: 800; color: var(--gold); white-space: nowrap; }

  .card-number {
    position: absolute; left: 24px; top: 124px; width: 440px;
    display: flex; justify-content: space-between;
    font-family: "Share Tech Mono", monospace; font-size: 38px; letter-spacing: 1px;
    color: #f1f4f8; text-shadow: 0 1px 1px rgba(0,0,0,0.5);
  }
  .expiry-label { position: absolute; left: 211px; top: 183px; font-size: 10px; color: #dfe6ee; }
  .valid-thru { position: absolute; left: 175px; top: 200px; font-size: 8px; line-height: 8px; color: #dfe6ee; }
  .expiry { position: absolute; left: 209px; top: 191px; font-family: "Share Tech Mono", monospace; font-size: 27px; color: #f1f4f8; }
  .holder { position: absolute; left: 24px; top: 244px; font-family: "Share Tech Mono", monospace; font-size: 19px; color: #f1f4f8; letter-spacing: 0.5px; }
  .card-type { position: absolute; right: 25px; top: 243px; font-size: 19px; font-weight: 800; font-style: italic; color: var(--gold); }

  .tagline-band {
    position: absolute; left: 0; top: 27px; width: 100%; height: 63px;
    background: var(--white); display: flex; align-items: center; justify-content: center;
    color: var(--ink); font-size: 21px; font-weight: 600; letter-spacing: 0.3px;
  }
  .signature-strip { position: absolute; left: 146px; top: 98px; width: 195px; height: 42px; background: var(--strip); }
  .signature-label { position: absolute; left: 145px; top: 143px; font-size: 8px; font-weight: 500; }
  .email { position: absolute; left: 0; width: 100%; top: 159px; text-align: center; font-size: 17px; font-weight: 500; letter-spacing: 0.3px; }
  .contact { position: absolute; left: 0; width: 100%; top: 181px; text-align: center; font-size: 11px; font-weight: 500; }

  .back-brand { left: 30px; top: 200px; width: 200px; height: 64px; }
  .back-brand .brand__tag { font-size: 5px; }
  .back-brand .brand__name { left: 0; top: 8px; font-size: 24px; gap: 6px; }
  .back-brand .brand__dot { width: 18px; height: 18px; }
  .back-brand .brand__sub { position: absolute; left: 55px; top: 36px; font-size: 12px; font-weight: 800; color: var(--gold); white-space: nowrap; }

  .social { position: absolute; right: 30px; top: 221px; display: flex; gap: 10px; }
  .social__dot { width: 41px; height: 41px; border-radius: 50%; }
  .social__dot--one { background: var(--dot-one); }
  .social__dot--two { background: var(--dot-two); }
  .social__dot--three { background: var(--dot-three); }
</style>
</head>
<body>

<section class="card card--front" aria-label="Business card front">
  <div class="map-area" role="img" aria-label="Faint dotted world map in the background"></div>

  <svg class="chip" viewBox="0 0 56 49" aria-hidden="true">
    <defs>
      <radialGradient id="chipGold" cx="0.55" cy="0.4" r="0.7">
        <stop offset="0" stop-color="var(--chip-light)"/>
        <stop offset="1" stop-color="var(--chip-dark)"/>
      </radialGradient>
    </defs>
    <rect x="0.5" y="0.5" width="55" height="48" rx="7" fill="url(#chipGold)" stroke="#8a6a1c" stroke-width="1"/>
    <g fill="none" stroke="#8a6a1c" stroke-width="1">
      <path d="M0 14 H18 M0 25 H18 M0 36 H18 M38 14 H56 M38 25 H56 M38 36 H56"/>
      <rect x="18" y="8" width="20" height="33" rx="3"/>
    </g>
  </svg>

  <div class="brand front-brand">
    <span class="brand__tag" style="left:78px;top:0">BUSINESS BROKER</span>
    <span class="brand__tag" style="left:184px;top:0">BUSINESS FUNDING</span>
    <div class="brand__name"><span class="brand__dot"></span>RELAY</div>
    <span class="brand__sub">Business Partners</span>
    <span class="brand__tag" style="left:78px;top:73px">CREDIT CARD PROCESSING</span>
    <span class="brand__tag" style="left:184px;top:73px">MERCHANT BROKER</span>
  </div>

  <div class="card-number"><span>0720</span><span>0104</span><span>0122</span><span>1208</span></div>
  <span class="expiry-label">MONTH/YEAR</span>
  <span class="valid-thru">VALID<br>THRU</span>
  <span class="expiry">12/50</span>
  <span class="holder">DANA WHITLOW / 307-555-0186</span>
  <span class="card-type">CREDIT CARD</span>
</section>

<section class="card card--back" aria-label="Business card back">
  <div class="map-area" role="img" aria-label="Faint dotted world map in the background"></div>
  <div class="tagline-band">Experience Better Credit Card Processing</div>
  <div class="signature-strip" role="img" aria-label="Signature panel with fine security text"></div>
  <span class="signature-label">AUTHORIZED SIGNATURE</span>
  <p class="email">RelayBizPartners@mailbox.com</p>
  <p class="contact">CONTACT US: 307-555-0186</p>

  <div class="brand back-brand">
    <span class="brand__tag" style="left:55px;top:0">BUSINESS BROKER</span>
    <span class="brand__tag" style="left:128px;top:0">BUSINESS FUNDING</span>
    <div class="brand__name"><span class="brand__dot"></span>RELAY</div>
    <span class="brand__sub">Business Partners</span>
    <span class="brand__tag" style="left:55px;top:53px">CREDIT CARD PROCESSING</span>
    <span class="brand__tag" style="left:128px;top:53px">MERCHANT BROKER</span>
  </div>

  <div class="social" aria-label="Social media links">
    <span class="social__dot social__dot--one"></span>
    <span class="social__dot social__dot--two"></span>
    <span class="social__dot social__dot--three"></span>
  </div>
</section>

</body>
</html>
```